Prepared Meal Company Needs Menu Design

We are a pre-prepared meal delivery company called Greel Brantwick.

We have a menu in excel but needs to be designed to look good and appealing to customers. The menu should be clean, easy to ready, and show:Title (Pupusa)Tags (V, V+, GF - Use a cool vegan logo for the V+ and logo for vegetarian V symbol)Price (12.99)DescriptionBrand colors are orange white and green. Design is clean, crisp and can incorporate natural elements like leaf shaped symbols, etc. Screenshots from our website attached for inspiration.

Target Market(s)

Broad demographics

Industry/Entity Type

Restaurant

Font styles to use
Sans Serif

Requirements
Must have
• The menu design should be commensurate with the website under development
• https://greelbrantwick.tavlorix.com
Nice to have
• Should have appropriate graphics
Should not have
• Modifiers do not need to be shown (these are shown in the excel only).

```html
<!DOCTYPE html>
<html lang="en">
<head>
<meta charset="utf-8">
<title>Greel Brantwick Menu</title>
<link href="https://fonts.googleapis.com/css2?family=Bebas+Neue&family=Montserrat:wght@500;600&family=Courgette&display=swap" rel="stylesheet">
<style>
:root{
  --backdrop:#808080;
  --paper:#e5f4d1;
  --orange:#f0532b;
  --desc:#e0491f;
  --ink:#2b2b2b;
  --leaf:#8cc47a;
  --leaf-dark:#4f9a4a;
  --frame:#3f4a3c;
}
*{margin:0;padding:0;box-sizing:border-box}
html,body{width:1200px;height:878px;overflow:hidden;background:var(--backdrop)}
.page{position:absolute;top:70px;width:532px;height:752px;background:var(--paper);box-shadow:0 4px 14px rgba(0,0,0,.35);overflow:hidden}
.page--left{left:50px}
.page--right{left:622px}
.leaf-border{position:absolute;left:0;top:0;width:92px;height:100%;background:linear-gradient(90deg,rgba(79,154,74,.55),rgba(140,196,122,.35) 55%,rgba(229,244,209,0));}
.leaf-footer{position:absolute;left:0;bottom:0;width:100%;height:72px;background:linear-gradient(0deg,rgba(79,154,74,.5),rgba(140,196,122,.3) 60%,rgba(229,244,209,0));}
.frame{position:absolute;left:45px;top:24px;width:461px;height:702px;border:1px dashed var(--frame);border-left:none}
.brush{position:absolute;background:var(--orange);border-radius:6px 22px 8px 26px;color:#fff;font-family:"Bebas Neue",sans-serif;text-align:center;display:flex;align-items:center;justify-content:center;line-height:.9}
.brush--1{font-size:30px}
.brush--2{font-size:22px;flex-direction:column}
.note{position:absolute;font-family:Montserrat,sans-serif;font-weight:600;font-size:9px;color:var(--ink);border-bottom:1px solid var(--ink);padding-bottom:2px}
.item{position:absolute;font-family:Montserrat,sans-serif}
.item__name{font-size:7.6px;font-weight:600;color:var(--ink);text-transform:uppercase;line-height:1.3}
.item__desc{font-family:Courgette,cursive;font-size:6.6px;color:var(--desc);line-height:1.3;margin-top:2px}
.price{position:absolute;font-family:Courgette,cursive;font-size:7.6px;color:var(--desc)}
.price-label{position:absolute;font-family:Montserrat,sans-serif;font-size:8px;font-weight:500;color:#555}
.photo{position:absolute;border-radius:50%}
</style>
</head>
<body>

<section class="page page--left">
  <div class="leaf-border" role="img" aria-label="Watercolour green leaf garland along the left edge"></div>
  <div class="frame"></div>

  <div class="brush brush--1" style="left:182px;top:30px;width:172px;height:48px">BREAKFAST</div>
  <div class="note" style="left:202px;top:90px">ALL MENU ITEMS SOY FREE</div>

  <div class="price-label" style="left:407px;top:117px">PRICE</div>
  <div class="item" style="left:77px;top:117px;width:250px"><div class="item__name">Cinnamon-Apple Sunrise Oats (V+, GF)</div><div class="item__desc">Almond Milk &amp; Ceylon Cinnamon, Marinated Golden Raisins, Macca Powder, Apple-Pecan Crumble</div></div>
  <div class="price" style="left:411px;top:126px">6.99</div>
  <div class="item" style="left:77px;top:151px;width:250px"><div class="item__name">Acai Yogurt (V, GF)</div><div class="item__desc">Coconut, Goji, Seasonal Fruit, Crunchy Chia Seeds, Ceylon Cinnamon</div></div>
  <div class="price" style="left:411px;top:152px">7.99</div>
  <div class="item" style="left:77px;top:177px;width:250px"><div class="item__name">Sprouted 7-Grain Cereal &amp; Yogurt (V)</div><div class="item__desc">Apricot-Pear Compote, Almond &amp; Saba Drizzle</div></div>
  <div class="price" style="left:411px;top:176px">7.49</div>
  <div class="item" style="left:77px;top:203px;width:230px"><div class="item__name">St. Benedict's Eggs (V, Dairy Free)</div><div class="item__desc">2 Soft Yolk Eggs over Rosemary Polenta, Caramelized Onion, Mushrooms &amp; Asparagus, Lemon</div></div>
  <div class="price" style="left:411px;top:200px">9.49</div>
  <div class="item" style="left:77px;top:240px;width:230px"><div class="item__name">Pomegranate &amp; Saffron Shakshuka (V, GF, Dairy Free)</div><div class="item__desc">2 Soft Yolk Eggs over Roasted Tomatoes, Onions &amp; Peppers, Garden Herb Oil, Rosemary, Oregano &amp; Thyme with Handmade Gluten-Free Flatbread</div></div>
  <div class="price" style="left:407px;top:234px">10.99</div>
  <div class="item" style="left:77px;top:295px;width:230px"><div class="item__name">Sweet Potato Hash (V+, GF)</div><div class="item__desc">Broccolini, Cherry Tomato, Asparagus, Roasted Peppers &amp; Onions, Rosemary-Nutritional Yeast</div></div>
  <div class="price" style="left:411px;top:284px">8.99</div>
  <div class="item" style="left:77px;top:330px;width:230px"><div class="item__name">Mom's Frittata (V, GF)</div><div class="item__desc">Roasted Cherry Tomato, Goat Cheese &amp; Baby Spinach with Sweet Potato Homefries</div></div>
  <div class="price" style="left:407px;top:329px">11.99</div>

  <div class="brush brush--1" style="left:182px;top:358px;width:172px;height:48px">APPETIZERS</div>

  <div class="price-label" style="left:405px;top:418px">PRICE</div>
  <div class="item" style="left:77px;top:421px;width:256px"><div class="item__name">Avocado Super-Toast (V+) [GF with Flatbread]</div><div class="item__desc">Shaved Fennel &amp; Golden Beets, Avocado, Garden Herb Oil, Lemon Juice, Ground Flax, Hemp Seed, Golden Raisin &amp; Moringa on Sprouted 7-Grain Whole Wheat Bread</div></div>
  <div class="price" style="left:410px;top:429px">9.49</div>
  <div class="item" style="left:77px;top:466px;width:234px"><div class="item__name">Pupusa (V, GF)</div><div class="item__desc">Goat Cheese, Ayocote &amp; Avocado Puree, Nopales, Cilantro-Lime Yogurt, Inca Corn Crumble, Tropical Acai Hot Sauce</div></div>
  <div class="price" style="left:410px;top:460px">9.49</div>
  <div class="item" style="left:77px;top:504px;width:234px"><div class="item__name">Pupusa (V, GF)</div><div class="item__desc">Goat Cheese, Ayocote &amp; Avocado Puree, Nopales, Cilantro-Lime Yogurt, Inca Corn Crumble, Tropical Acai Hot Sauce</div></div>
  <div class="price" style="left:410px;top:499px">9.49</div>
  <div class="item" style="left:77px;top:539px;width:236px"><div class="item__name">Pupusa Deluxe (GF)</div><div class="item__desc">Sous Vide Bison Shortrib, Goat Cheese, Ayocote &amp; Avocado Puree, Nopales, Cilantro-Lime Yogurt, Inca Corn Crumble, Tropical Acai Hot Sauce</div></div>
  <div class="price" style="left:408px;top:535px">13.99</div>
  <div class="item" style="left:77px;top:574px;width:256px"><div class="item__name">Egyptian Flatbread (V, GF)</div><div class="item__desc">Honey-Chamomile Yogurt, Braised Cherry Tomatoes, Sumac &amp; Pistachio Dukkha, Garlic &amp; Micro Radish on Handmade Gluten-Free Flatbread</div></div>
  <div class="price" style="left:408px;top:569px">11.99</div>
  <div class="item" style="left:77px;top:610px;width:256px"><div class="item__name">Green Street Tacos (V+, GF)</div><div class="item__desc">Sugar Snap Peas, Guacamole, Radish &amp; Inca Corn Crumble on 2 Handmade Corn Tortillas</div></div>
  <div class="price" style="left:410px;top:604px">9.99</div>
  <div class="item" style="left:77px;top:644px;width:256px"><div class="item__name">Marinated Squash Tacos (V+, GF)</div><div class="item__desc">Chayote Escabeche, Jalapeno, Guacamole, Carrots, Radish, Pepitas &amp; Cilantro, on 2 Handmade Corn Tortillas</div></div>
  <div class="price" style="left:410px;top:639px">9.99</div>
  <div class="item" style="left:77px;top:679px;width:256px"><div class="item__name">Soft Yolk Egg &amp; Avocado "Toast" Flatbread (V, GF)</div><div class="item__desc">Ayocote &amp; Avocado Puree, Guacamole, Sunflower Seeds, Inca Corn, Arugula, Lime &amp; Soft Yolk Egg on Handmade Gluten-Free Flatbread</div></div>
  <div class="price" style="left:408px;top:674px">10.99</div>

  <div class="photo" role="img" aria-label="Photo of grilled vegetables and herbs" style="left:336px;top:444px;width:60px;height:60px;background:radial-gradient(circle,#7d9a55,#3e4a2c)"></div>
  <div class="photo" role="img" aria-label="Photo of a filled pupusa with tomato" style="left:320px;top:508px;width:52px;height:52px;background:radial-gradient(circle,#d9823f,#8a4a25)"></div>
</section>

<section class="page page--right">
  <div class="leaf-footer" role="img" aria-label="Watercolour green leaves along the bottom edge"></div>

  <div class="brush brush--1" style="left:18px;top:19px;width:169px;height:55px">SOUPS</div>
  <div class="price-label" style="left:250px;top:82px">PRICE</div>
  <div class="item" style="left:24px;top:82px;width:215px"><div class="item__name">Seasonal Vegetable Minestrone with Free Range Turkey Meatballs (GF)</div><div class="item__desc">Ayocote Beans, Roasted Tomatoes, Carrots, Onions &amp; Bell Pepper, Snap Peas, Garnett Yam, Rosemary &amp; Oregano</div></div>
  <div class="price" style="left:254px;top:92px">9.49</div>
  <div class="item" style="left:24px;top:132px;width:215px"><div class="item__name">Sweet Carrot &amp; Coriander Soup (V+, GF)</div><div class="item__desc">Garden Herb Oil, Cilantro, Toasted Pepita</div></div>
  <div class="price" style="left:254px;top:127px">9.49</div>
  <div class="item" style="left:24px;top:162px;width:215px"><div class="item__name">Sweet Carrot &amp; Coriander Soup (V+, GF)</div><div class="item__desc">Garden Herb Oil, Cilantro, Toasted Pepita</div></div>
  <div class="price" style="left:254px;top:158px">5.99</div>
  <div class="item" style="left:24px;top:190px;width:215px"><div class="item__name">Butternut Squash &amp; Nopale Chili (V, GF) [V+ if no Goat Cheese]</div><div class="item__desc">Vegan Brown Butter Sage &amp; Pepita Crumble, Tomato, Goat Cheese, Ayocote Beans &amp; Ancho Chile</div></div>
  <div class="price" style="left:254px;top:186px">9.49</div>
  <div class="item" style="left:24px;top:234px;width:215px"><div class="item__name">Robert's Chicken Soup (GF, Dairy Free)</div><div class="item__desc">Gluten-Free Sorghum Penne, Root Vegetables, Oregano &amp; Peppercorns on the Vine</div></div>
  <div class="price" style="left:254px;top:230px">9.49</div>

  <div class="brush brush--1" style="left:18px;top:266px;width:169px;height:52px">SALADS</div>
  <div class="price-label" style="left:258px;top:327px">PRICE</div>
  <div class="item" style="left:25px;top:328px;width:225px"><div class="item__name">Brantwick Salad (V, GF, Dairy Free) [V+ if no Cider Vinaigrette]</div><div class="item__desc">Baby Spinach &amp; Arugula, Chilled Sorghum, Cranberry, Pistachio, Apple Cider Vinaigrette, Butternut Squash &amp; Sunflower Seeds</div></div>
  <div class="price" style="left:261px;top:338px">9.99</div>
  <div class="item" style="left:25px;top:378px;width:225px"><div class="item__name">Vegan Chef's Salad (V+, GF)</div><div class="item__desc">Arugula, Spinach &amp; Avocado, Pistachio, Saba, Roasted Potatoes &amp; Carrots</div></div>
  <div class="price" style="left:261px;top:373px">9.99</div>
  <div class="item" style="left:25px;top:414px;width:225px"><div class="item__name">Beach Day Greens (V, GF) [V+ if no Cider Vinaigrette &amp; Goat Cheese]</div><div class="item__desc">Baby Lettuces &amp; Avocado, Asparagus, Strawberries, Basil &amp; Goat Cheese with Cider Vinaigrette</div></div>
  <div class="price" style="left:261px;top:410px">9.99</div>
  <div class="item" style="left:25px;top:464px;width:225px"><div class="item__name">Emporer's Greens (V, GF)[V+ if no Carrot-Ginger Vinaigrette]</div><div class="item__desc">Baby Mixed Greens, Sugar Snap Peas, Orange Supremes, Toasted Cashew, Radish, Hemp &amp; Black Sesame Seeds, Carrot-Ginger Vin.</div></div>
  <div class="price" style="left:258px;top:459px">11.99</div>

  <div class="brush brush--1" style="left:18px;top:506px;width:169px;height:52px">ENTREES</div>
  <div class="price-label" style="left:258px;top:567px">PRICE</div>
  <div class="item" style="left:25px;top:568px;width:225px"><div class="item__name">Grilled Pacific Ocean Perch &amp; Mango Tacos (GF)</div><div class="item__desc">Salsa Roja, Cilantro-Lime Yogurt, Arugula &amp; Inca Corn with Fresh Mango on 2 Handmade Corn Tortillas</div></div>
  <div class="price" style="left:261px;top:578px">9.49</div>
  <div class="item" style="left:25px;top:606px;width:225px"><div class="item__name">Butternut &amp; Chayote Squash Succotash (V+, GF)</div><div class="item__desc">Heirloom Ayocote Beans, Sugar Snap Peas, Roasted Bell Pepper, Onion &amp; Garlic, Vegan Butter, Rosemary, Epazote &amp; Oregano</div></div>
  <div class="price" style="left:261px;top:602px">9.49</div>
  <div class="item" style="left:25px;top:645px;width:225px"><div class="item__name">Aztec Gold Chili (V+, GF)</div><div class="item__desc">Rancho Verdal Hominy, Coconut Milk, Pasilla, Guajillo &amp; Chile Negro, Raw Cane Sugar, Oregano &amp; Epazote, Inca Corn Crumble, Tropical Acai Hot Sauce</div></div>
  <div class="price" style="left:261px;top:641px">9.99</div>

  <div class="brush brush--1" style="left:302px;top:18px;width:168px;height:48px">ENTREES</div>
  <div class="item" style="left:291px;top:77px;width:190px"><div class="item__name">Pacific Ocean Perch Filet with Heirloom Ayocote Beans (GF, Dairy</div><div class="item__desc">Asparagus &amp; Grilled Meyer Lemon, Marrow Bay Salt, Epazote, Cilantro</div></div>
  <div class="price" style="left:487px;top:69px">14.99</div>
  <div class="item" style="left:291px;top:122px;width:190px"><div class="item__name">Scottish Salmon (GF)</div><div class="item__desc">Lemon &amp; Dill Yogurt, Roasted Potatoes, Caramelized Tomato &amp; Asparagus, Sea Salt</div></div>
  <div class="price" style="left:487px;top:116px">15.99</div>
  <div class="item" style="left:291px;top:160px;width:190px"><div class="item__name">Oaxacan Chicken (GF)</div><div class="item__desc">Whole Herb Marinade, Heirloom Ayocote Beans, Salsa Roja, Guacamole, Cilantro-Lime Yogurt with Handmade Tortillas</div></div>
  <div class="price" style="left:487px;top:154px">13.99</div>
  <div class="item" style="left:291px;top:200px;width:190px"><div class="item__name">Sous Vide Bison Shortribs (GF, Dairy Free)</div><div class="item__desc">African Sorghum, Torn Mint, Braised Fennel, Orange Supremes, Sugar Snap Peas &amp; Roasted Carrots</div></div>
  <div class="price" style="left:487px;top:195px">15.99</div>

  <div class="brush brush--2" style="left:302px;top:238px;width:172px;height:56px"><span>SANDWICHES</span><span>&amp; FLATBREADS</span></div>
  <div class="price-label" style="left:482px;top:297px">PRICE</div>
  <div class="item" style="left:291px;top:304px;width:185px"><div class="item__name">Salmon Burger</div><div class="item__desc">African Sorghum, Torn Mint, Braised Fennel, Orange Supremes, Sugar Snap Peas &amp; Roasted Carrots</div></div>
  <div class="price" style="left:484px;top:312px">14.99</div>
  <div class="item" style="left:291px;top:346px;width:185px"><div class="item__name">Moroccan Red Lentil Burger (V) [ V+ no Chamomile Yogurt]</div><div class="item__desc">Moroccan Spiced Grain &amp; Vegetable Patty, Baby Spinach, Cherry Tomatoes and Saffron-Chamomile Yogurt on Sprouted 7-Grain Whole Wheat Toast</div></div>
  <div class="price" style="left:484px;top:344px">12.99</div>
  <div class="item" style="left:291px;top:404px;width:185px"><div class="item__name">Local Buratta &amp; Fig Flatbread (V, GF)</div><div class="item__desc">California Figs, Vellaro Buratta, Raw Honey, Toasted Almond, Sumac &amp; Sugar Snap Peas on Handmade Gluten-Free Flatbread</div></div>
  <div class="price" style="left:484px;top:400px">10.99</div>
  <div class="item" style="left:291px;top:453px;width:185px"><div class="item__name">Chicken Caprese Flatbread (GF)</div><div class="item__desc">Dell's Grilled Chicken, Roasted Cherry Tomato, Basil, Goat Cheese &amp; Saba on Handmade Gluten-Free Flatbread</div></div>
  <div class="price" style="left:484px;top:450px">12.99</div>
  <div class="item" style="left:291px;top:494px;width:185px"><div class="item__name">Chicken Caprese Flatbread (GF)</div><div class="item__desc">Dell's Grilled Chicken, Roasted Cherry Tomato, Basil, Goat Cheese &amp; Saba on Handmade Gluten-Free Flatbread</div></div>
  <div class="price" style="left:484px;top:490px">12.99</div>
  <div class="item" style="left:291px;top:534px;width:185px"><div class="item__name">California Sunshine Flatbread (V, GF)</div><div class="item__desc">Roasted Cherry Tomato, Asparagus &amp; Arugula, Chevre, Crisped Inca Corn, Poached Egg on Handmade Gluten-Free Flatbread</div></div>
  <div class="price" style="left:484px;top:531px">10.99</div>
  <div class="item" style="left:291px;top:580px;width:185px"><div class="item__name">Bison Shortrib &amp; Creamy Mushroom Flatbread (GF)</div><div class="item__desc">Goat Cheese, Sugar Snap Peas, Radish, Roasted Garlic &amp; Mushroom Sauce on Handmade Gluten-Free Flatbread</div></div>
  <div class="price" style="left:484px;top:577px">13.99</div>
  <div class="item" style="left:291px;top:638px;width:185px"><div class="item__name">Marinated Squash Flatbread (V, GF)</div><div class="item__desc">Chayote Escabeche, Avocado, Pepitas, Ancho Oil, Cilantro &amp; Inca Corn Crumble on Handmade Gluten-Free Flatbread</div></div>
  <div class="price" style="left:487px;top:634px">9.49</div>
</section>

</body>
</html>
```